Funky Cloud Security Startup wants a cutting edge website

We're looking for a clean and simple website to be able to sell out cutting edge Cloud Security products. We already have a logo and business codes to give you a view of the style/colours etc (see attached). Really looking for something similar to brimlo.com , vadrine.com and if push comes to shove then our competitors tandry pelwick.com.au don't have a bad site either.

We're still working through the content sections but want to have a home for the following types of content immediately:

Products (4 of them)
Company
Technology Partners
Press/News
Contact Us
Support
Login

and the site will need to expand to accommodate

Buy
Case Studies
Channel Partners

at some point in the future

On the bottom Nav we want:
* Privacy Policy
* Terms of Use
* Contact
* Vantiqo
* Plimsy

The home page should an image rotator on it with some suitably cool images and call to actions as text hovering over them.

We need it to be easily editable in dreamweaver so a template is a must, it should also be completely CSS driven and adaptive so will work on mobile, tablet and desktop - you know the score.

We're hosting on a linux server so PHP code for any crazy stuff is a must.

Really exciting project as this will be a huge company with major investors backing it internationally so you will be able to put your name against the next Quorvix/Plimsy/Zembro.

Go crazy with your creativity, just remember kurvo's slogan is "Security made simple"

We look forward to seeing your creations, good luck!

```html
<!DOCTYPE html>
<html lang="en">
<head>
<meta charset="utf-8">
<title>kurvo — Security made Simple</title>
<link rel="stylesheet" href="https://fonts.googleapis.com/css2?family=Open+Sans:wght@300;400;600;700&display=swap">
<style>
  :root {
    --ink: #555b60;
    --ink-soft: #8a8f93;
    --ink-dark: #2b2f33;
    --brand-blue: #1d6f99;
    --accent-blue: #2aa0d6;
    --hero-bg: #0b1e27;
    --hero-glow: #1b6c8c;
    --rule: #e3e5e7;
    --footer-bg: #f1f2f3;
    --white: #ffffff;
  }
  * { box-sizing: border-box; margin: 0; padding: 0; }
  html, body { width: 1200px; height: 879px; overflow: hidden; }
  body {
    font-family: "Open Sans", Arial, sans-serif;
    background: var(--white);
    color: var(--ink);
    position: relative;
  }
  a { color: inherit; text-decoration: none; }

  /* Header */
  .site-header {
    position: absolute; left: 0; top: 0; width: 1200px; height: 100px;
    background: linear-gradient(#ffffff 0%, #ffffff 55%, #f1f2f3 100%);
    border-top: 1px solid var(--rule);
  }
  .brand {
    position: absolute; left: 96px; top: 28px;
    display: flex; align-items: center; gap: 10px;
  }
  .brand-dot {
    width: 40px; height: 40px; border-radius: 50%;
    background: var(--accent-blue);
  }
  .brand-name {
    font-size: 46px; font-weight: 400; color: #58595b; letter-spacing: -1px; line-height: 1;
  }
  .main-nav {
    position: absolute; right: 94px; top: 48px;
    display: flex; gap: 25px; font-size: 16px; color: var(--ink);
  }
  .main-nav .nav-login { color: var(--brand-blue); font-weight: 600; }

  /* Hero */
  .hero {
    position: absolute; left: 0; top: 100px; width: 1200px; height: 504px;
    background: var(--hero-bg);
  }
  .hero-visual {
    position: absolute; left: 210px; top: 0; width: 790px; height: 504px;
    background: radial-gradient(ellipse at 50% 55%, var(--hero-glow) 0%, #123847 40%, var(--hero-bg) 85%);
  }
  .hero-title {
    position: absolute; left: 0; right: 0; top: 190px;
    text-align: center; color: var(--white);
    font-size: 64px; font-weight: 400; letter-spacing: -0.5px;
  }
  .hero-arrow { position: absolute; top: 186px; }
  .hero-arrow.prev { left: 54px; }
  .hero-arrow.next { right: 42px; }

  /* Features */
  .features {
    position: absolute; left: 0; top: 604px; width: 1200px; height: 196px;
    display: flex; border-bottom: 1px solid var(--rule);
  }
  .feature {
    position: relative; height: 100%;
    border-right: 1px solid var(--rule);
  }
  .feature:nth-child(1) { width: 422px; }
  .feature:nth-child(2) { width: 354px; }
  .feature:nth-child(3) { width: 424px; border-right: none; }
  .feature-media {
    position: absolute; top: 32px; width: 132px; height: 134px;
  }
  .feature:nth-child(1) .feature-media { left: 94px; background: linear-gradient(135deg, #2c7fc4, #1a3f6e 60%, #c0393a); }
  .feature:nth-child(2) .feature-media { left: 27px; background: linear-gradient(160deg, #4aa6cf, #174a68 70%); }
  .feature:nth-child(3) .feature-media { left: 26px; background: linear-gradient(135deg, #d6d8d8, #6f7374 60%, #2e3132); }
  .feature-body { position: absolute; top: 28px; }
  .feature:nth-child(1) .feature-body { left: 239px; }
  .feature:nth-child(2) .feature-body { left: 172px; }
  .feature:nth-child(3) .feature-body { left: 171px; }
  .feature-title {
    font-size: 20px; font-weight: 400; color: var(--accent-blue); line-height: 26px;
  }
  .feature-text {
    margin-top: 2px; width: 160px;
    font-size: 11.5px; line-height: 18px; color: var(--ink-soft);
  }
  .feature-link {
    display: block; margin-top: 3px;
    font-size: 13px; font-weight: 700; color: var(--ink-dark);
  }

  /* Footer */
  .site-footer {
    position: absolute; left: 0; top: 800px; width: 1200px; height: 79px;
    background: var(--footer-bg);
    font-size: 13px; color: var(--ink);
  }
  .footer-legal { position: absolute; left: 93px; top: 30px; }
  .footer-nav {
    position: absolute; right: 92px; top: 27px;
    display: flex; align-items: center; gap: 9px;
  }
  .footer-nav .sep { color: #aaa; }
  .social { display: flex; align-items: center; gap: 5px; margin-left: 6px; }
  .social-dot { width: 10px; height: 10px; border-radius: 50%; background: #666; }
</style>
</head>
<body>
  <header class="site-header">
    <a class="brand" href="#"><span class="brand-dot"></span><span class="brand-name">kurvo.</span></a>
    <nav class="main-nav">
      <a href="#">Home</a>
      <a href="#">Products</a>
      <a href="#">Company</a>
      <a href="#">Technology Partners</a>
      <a href="#">Press/News</a>
      <a href="#">Contact Us</a>
      <a href="#">Support</a>
      <a href="#" class="nav-login">Login</a>
    </nav>
  </header>

  <section class="hero">
    <div class="hero-visual" role="img" aria-label="Glowing blue cloud with a padlock over a field of hexadecimal code"></div>
    <svg class="hero-arrow prev" width="42" height="100" viewBox="0 0 42 100" aria-hidden="true">
      <polyline points="40,2 2,50 40,98" fill="none" stroke="#8c9aa1" stroke-width="2"/>
    </svg>
    <svg class="hero-arrow next" width="42" height="100" viewBox="0 0 42 100" aria-hidden="true">
      <polyline points="2,2 40,50 2,98" fill="none" stroke="#8c9aa1" stroke-width="2"/>
    </svg>
    <h1 class="hero-title">Security made Simple</h1>
  </section>

  <section class="features">
    <article class="feature">
      <div class="feature-media" role="img" aria-label="Red cloud icon inside a blue circle of arrows"></div>
      <div class="feature-body">
        <h2 class="feature-title">WHY SECURITY</h2>
        <p class="feature-text">Etiam est nunc venenatis in tristique eu imperdiet ac nisl Cum sociis natoque penati-bus et magnis dis parturient montes nascetur</p>
        <a class="feature-link" href="#">LEARN MORE</a>
      </div>
    </article>
    <article class="feature">
      <div class="feature-media" role="img" aria-label="Businessman touching a glowing cloud lock icon"></div>
      <div class="feature-body">
        <h2 class="feature-title">OUR SERVICES</h2>
        <p class="feature-text">Etiam est nunc venenatis in tristique eu imperdiet ac nisl Cum sociis natoque penati-bus et magnis dis parturient montes nascetur</p>
        <a class="feature-link" href="#">LEARN MORE</a>
      </div>
    </article>
    <article class="feature">
      <div class="feature-media" role="img" aria-label="Hand reaching toward a cluster of grey clouds"></div>
      <div class="feature-body">
        <h2 class="feature-title">TECHNOLOGY</h2>
        <p class="feature-text">Etiam est nunc venenatis in tristique eu imperdiet ac nisl Cum sociis natoque penati-bus et magnis dis parturient montes nascetur</p>
        <a class="feature-link" href="#">LEARN MORE</a>
      </div>
    </article>
  </section>

  <footer class="site-footer">
    <p class="footer-legal">© 2014 Company Name.&nbsp; All right reserved.&nbsp; Term of Use</p>
    <nav class="footer-nav">
      <a href="#">Privacy Policy</a><span class="sep">|</span>
      <a href="#">Terms of Use</a><span class="sep">|</span>
      <a href="#">Contact</a>
      <a class="social" href="#"><span class="social-dot"></span>Vantiqo</a>
      <a class="social" href="#"><span class="social-dot"></span>Plimsy</a>
    </nav>
  </footer>
</body>
</html>
```